Kestrel Roofing & Restoration Business Card Design

Lookiing for a double sided business card design that will have rounded corners, will look good with Spot UV, Soft Laminate, or Gloss
Front of card should have Logo, Name and Contact Info, License numbers
Back of card should have Logo, maybe other small details

```html
<!DOCTYPE html>
<html lang="en">
<head>
<meta charset="utf-8">
<title>Kestrel Roofing &amp; Restoration – Business Card</title>
<link rel="stylesheet" href="https://fonts.googleapis.com/css2?family=Montserrat:wght@700&family=Arimo:wght@400&display=swap">
<style>
  :root {
    --paper: #e9e9e7;
    --card: #2c2c2c;
    --card-deep: #262626;
    --blue: #0a9bd8;
    --band: #e4e4e4;
    --white: #ffffff;
    --muted: #b8b8b8;
    --emboss: #6e6e6e;
  }
  * { margin: 0; padding: 0; box-sizing: border-box; }
  html, body { width: 1200px; height: 801px; overflow: hidden; background: var(--paper); }
  .stage { position: relative; width: 1200px; height: 801px; }
  .card {
    position: absolute; top: 246px; width: 540px; height: 309px;
    border-radius: 12px; overflow: hidden; background: var(--card);
    box-shadow: 0 0 0 3px var(--blue), 0 14px 30px rgba(0,0,0,.18);
  }
  .card-front { left: 40px; }
  .card-back { left: 620px; background: var(--card-deep); }
  .card-art { position: absolute; inset: 0; }
  .brand {
    position: absolute; display: flex; align-items: center; gap: 14px;
    font-family: "Montserrat", sans-serif; font-weight: 700; color: var(--white);
  }
  .brand-mark { width: 16px; height: 16px; background: var(--blue); flex: none; }
  .brand-name { font-size: 21px; line-height: 1.1; letter-spacing: .5px; text-transform: uppercase; white-space: nowrap; }
  .card-front .brand { left: 42px; top: 88px; }
  .card-back .brand { left: 50%; top: 50%; transform: translate(-50%, -50%); color: var(--emboss); gap: 18px; }
  .card-back .brand-name { font-size: 30px; }
  .card-back .brand-mark { width: 22px; height: 22px; background: var(--emboss); }
  .holder {
    position: absolute; right: 40px; top: 46px; text-align: right;
    font-family: "Arimo", sans-serif;
  }
  .holder-name { color: var(--blue); font-size: 20px; letter-spacing: .5px; text-transform: uppercase; }
  .holder-role { color: var(--white); font-size: 13px; margin-top: 3px; }
  .contact {
    position: absolute; left: 52px; top: 166px; list-style: none;
    font-family: "Arimo", sans-serif; font-size: 14px; color: var(--white);
  }
  .contact li { display: flex; align-items: center; gap: 7px; height: 19px; }
  .contact svg { width: 12px; height: 12px; flex: none; }
  .licence {
    position: absolute; left: 52px; top: 234px;
    font-family: "Arimo", sans-serif; font-size: 12px; color: var(--muted);
  }
  .address {
    position: absolute; left: 72px; bottom: 14px;
    font-family: "Arimo", sans-serif; font-size: 15px; color: #333;
  }
</style>
</head>
<body>
<main class="stage">
  <section class="card card-front" aria-label="Card front">
    <svg class="card-art" viewBox="0 0 540 309" aria-hidden="true">
      <rect x="512" y="0" width="28" height="20" fill="var(--blue)"/>
      <polygon points="0,309 0,300 20,262 420,262 452,188 540,196 540,309" fill="var(--blue)"/>
      <polygon points="0,309 8,309 26,270 425,270 456,198 540,206 540,309" fill="var(--card)"/>
      <polygon points="30,309 45,276 430,276 460,206 540,214 540,309" fill="var(--band)"/>
    </svg>
    <div class="brand">
      <span class="brand-mark"></span>
      <span class="brand-name">Kestrel Roofing &amp;<br>Restoration</span>
    </div>
    <div class="holder">
      <p class="holder-name">Daniel Marsh</p>
      <p class="holder-role">Managing Director</p>
    </div>
    <ul class="contact">
      <li><svg viewBox="0 0 12 12"><path d="M3 1 L5 3.5 L4 5 Q5 7 7 8 L8.5 7 L11 9 L10 11 Q4 11 1 4 Z" fill="var(--blue)"/></svg>044-310 882 417</li>
      <li><svg viewBox="0 0 12 12"><rect x="1" y="3" width="10" height="7" fill="var(--blue)"/><path d="M1 3 L6 7 L11 3" stroke="var(--card)" fill="none"/></svg>info@kestrelroof.com</li>
      <li><svg viewBox="0 0 12 12"><circle cx="6" cy="6" r="5.5" fill="var(--blue)"/><path d="M1 6 H11 M6 .5 Q3 6 6 11.5 M6 .5 Q9 6 6 11.5" stroke="var(--card)" stroke-width=".8" fill="none"/></svg>www.kestrelroof.com</li>
    </ul>
    <p class="licence">Lic. No. KR-48213 &nbsp;|&nbsp; Builder Lic. 1290674</p>
    <p class="address">18 Harbour Lane, Westfield, State, Zip 4820</p>
  </section>

  <section class="card card-back" aria-label="Card back">
    <div class="brand">
      <span class="brand-mark"></span>
      <span class="brand-name">Kestrel Roofing &amp;<br>Restoration</span>
    </div>
  </section>
</main>
</body>
</html>
```